Wattle Glen Manor Brochure Design

We need a brochure designed for our Aged Care Facility. We need designs that portray warmth and welcoming and at the same time something professional. We have attached the previous brochure and are looking for a modern professional brochure. We are not set on sizing and welcome ideas.

Attachments:
- One more high res photo is available via this link: https://www.filevaultex.net/s/kq52wpx9trmbe3n/Manor_High-Res_18.jpg?dl=0
- Another high res file has been added and is available through this link:
https://www.filevaultex.net/s/mv71cnd8yhsue6r/Manor_High-Res_24.jpg?dl=0

Target Market(s)

Aged Care and families

Requirements
Must have
• Logo and contact details

```html
<!DOCTYPE html>
<html lang="en">
<head>
<meta charset="utf-8">
<title>Wattle Glen Manor – Trifold Brochure</title>
<link rel="stylesheet" href="https://fonts.googleapis.com/css2?family=Open+Sans:ital,wght@0,400;0,600;0,700;1,400;1,600;1,700&family=Roboto+Condensed:wght@400;700&display=swap">
<style>
  :root {
    --navy: #0d3f5e;
    --navy-deep: #083048;
    --sky: #2f8fd6;
    --sky-light: #5aaef0;
    --slate: #4d7187;
    --ink: #2b3e4c;
    --muted: #6b7882;
    --paper: #ffffff;
    --pale: #cfdde7;
    --bg: #e4e5e7;
  }
  * { box-sizing: border-box; margin: 0; padding: 0; }
  html, body { width: 1200px; height: 839px; overflow: hidden; background: var(--bg); }
  body { font-family: "Open Sans", sans-serif; color: var(--ink); }

  .brochure {
    position: absolute; left: 30px; top: 30px;
    width: 1140px; height: 779px;
    display: flex;
    box-shadow: 0 6px 24px rgba(0,0,0,.15);
  }
  .panel { position: relative; width: 380px; height: 779px; overflow: hidden; background: var(--paper); }
  .panel svg.shapes { position: absolute; inset: 0; }
  .panel .content { position: absolute; }

  /* Inside left panel */
  .intro { left: 30px; right: 30px; top: 360px; text-align: center; }
  .intro-lead { font-style: italic; font-size: 19px; line-height: 1.25; color: var(--muted); }
  .intro-lead strong { color: var(--ink); font-weight: 700; }
  .intro-body { margin-top: 26px; font-style: italic; font-size: 16px; line-height: 1.45; color: var(--muted); }

  .testimonial { left: 36px; right: 36px; top: 580px; text-align: center; color: var(--paper); }
  .quote-mark { font-family: "Open Sans", sans-serif; font-weight: 700; font-size: 60px; line-height: 46px; height: 40px; overflow: hidden; color: var(--sky-light); }
  .quote-text { margin-top: 8px; font-style: italic; font-size: 13px; line-height: 1.5; }
  .quote-name { margin-top: 10px; font-style: italic; font-weight: 700; font-size: 16px; }

  /* Back contact panel */
  .contact { left: 20px; right: 20px; top: 262px; text-align: center; }
  .brand { display: flex; align-items: center; justify-content: center; gap: 10px; white-space: nowrap; }
  .brand-dot { width: 30px; height: 30px; border-radius: 50%; background: var(--slate); flex: none; }
  .brand-name { font-family: "Roboto Condensed", sans-serif; font-weight: 400; font-size: 24px; letter-spacing: 1.5px; text-transform: uppercase; color: var(--slate); }
  .contact-title { margin-top: 30px; font-family: "Roboto Condensed", sans-serif; font-weight: 700; font-size: 30px; color: var(--navy); text-transform: uppercase; line-height: 1; }
  .contact-sub { margin-top: 2px; font-family: "Roboto Condensed", sans-serif; font-size: 19px; color: var(--muted); text-transform: uppercase; letter-spacing: .5px; }
  .contact-item { margin-top: 16px; font-size: 15px; line-height: 1.3; color: var(--ink); }
  .contact-item svg { display: block; margin: 0 auto 4px; }
  .contact-web { font-size: 16px; }

  /* Front cover panel */
  .cover-brand { left: 10px; right: 24px; top: 46px; text-align: center; }
  .cover-brand .brand-name { color: var(--pale); font-size: 22px; }
  .cover-brand .brand-dot { width: 26px; height: 26px; }
  .cover-line { margin-top: 20px; font-size: 9px; letter-spacing: 3px; color: var(--pale); text-transform: uppercase; }
  .cover-line small { display: block; font-size: 7.5px; letter-spacing: .5px; margin-top: 3px; }
  .cover-headline { left: 20px; right: 20px; top: 558px; text-align: center; font-family: "Roboto Condensed", sans-serif; font-weight: 700; font-size: 21px; line-height: 1.2; color: var(--paper); text-transform: uppercase; }
  .cover-web { left: 0; right: 0; top: 712px; text-align: center; font-size: 13px; letter-spacing: 2px; color: var(--pale); }
</style>
</head>
<body>
<main class="brochure">

  <section class="panel panel-intro">
    <svg class="shapes" width="380" height="779" viewBox="0 0 380 779">
      <defs>
        <linearGradient id="residentTone" x1="0" y1="0" x2="1" y2="1">
          <stop offset="0" stop-color="#d9c9a6"/>
          <stop offset=".5" stop-color="#e8ebe6"/>
          <stop offset="1" stop-color="#c9d3d6"/>
        </linearGradient>
        <linearGradient id="introFade" x1="0" y1="0" x2="0" y2="1">
          <stop offset="0" stop-color="#ffffff"/>
          <stop offset="1" stop-color="#f1f1f1"/>
        </linearGradient>
      </defs>
      <rect width="380" height="340" fill="url(#residentTone)" role="img" aria-label="Photo of a smiling resident seated in a bright lounge corridor"/>
      <path d="M0,335 C140,335 240,320 300,250 C330,215 350,200 380,198 L380,779 L0,779 Z" fill="url(#introFade)"/>
      <path d="M0,335 C140,335 240,320 300,250 C330,215 350,200 380,198" fill="none" stroke="var(--sky-light)" stroke-width="4"/>
      <path d="M0,565 C150,565 250,545 320,525 C350,516 365,520 380,528 L380,779 L0,779 Z" fill="var(--navy)"/>
      <path d="M0,556 C150,556 250,536 320,516 C350,507 365,511 380,519" fill="none" stroke="var(--sky-light)" stroke-width="4"/>
    </svg>
    <div class="content intro">
      <p class="intro-lead"><strong>Wattle Glen Manor</strong> is an accredited Government funded place...</p>
      <p class="intro-body">...aged care facility offering quality dignity and individuality for residents and their loved ones.</p>
    </div>
    <div class="content testimonial">
      <div class="quote-mark">&ldquo;</div>
      <p class="quote-text">Overall our mother is happier, she initiates conversation, her memory has improved. She laughs a lot &amp; still beats some of us at maths. Her &ldquo;spark&rdquo; seems to have returned. That makes the whole family happy.</p>
      <p class="quote-name">Maree Holden</p>
    </div>
  </section>

  <section class="panel panel-contact">
    <svg class="shapes" width="380" height="779" viewBox="0 0 380 779">
      <defs>
        <linearGradient id="roomTone" x1="0" y1="0" x2="1" y2="1">
          <stop offset="0" stop-color="#e9e4d8"/>
          <stop offset=".6" stop-color="#b7a792"/>
          <stop offset="1" stop-color="#6e6158"/>
        </linearGradient>
        <linearGradient id="contactFade" x1="0" y1="0" x2="1" y2="0">
          <stop offset="0" stop-color="#f3f3f3"/>
          <stop offset=".5" stop-color="#ffffff"/>
          <stop offset="1" stop-color="#e8e8e8"/>
        </linearGradient>
      </defs>
      <rect width="380" height="250" fill="url(#roomTone)" role="img" aria-label="Photo of a furnished resident bedroom with lounge chair and television"/>
      <path d="M0,198 C0,172 20,206 60,206 L380,206 L380,779 L0,779 Z" fill="url(#contactFade)"/>
      <path d="M0,198 C0,172 20,206 60,206 L380,206" fill="none" stroke="var(--sky-light)" stroke-width="4"/>
      <path d="M0,650 L260,650 C300,650 320,665 340,675 C355,682 370,680 380,676 L380,779 L0,779 Z" fill="var(--navy)"/>
      <path d="M0,642 L260,642 C300,642 320,657 340,667 C355,674 370,672 380,668" fill="none" stroke="var(--sky-light)" stroke-width="4"/>
    </svg>
    <div class="content contact">
      <div class="brand"><span class="brand-dot"></span><span class="brand-name">Wattle Glen Manor</span></div>
      <h2 class="contact-title">Contact us today</h2>
      <p class="contact-sub">For more information</p>
      <p class="contact-item">
        <svg width="18" height="18" viewBox="0 0 18 18"><circle cx="9" cy="9" r="8" fill="none" stroke="var(--navy)" stroke-width="1.5"/><path d="M6 5.5 L7.5 5 L8.3 7 L7.4 7.8 C7.9 8.9 8.7 9.8 9.9 10.4 L10.8 9.6 L12.6 10.5 L12.2 12 C9 12 5.8 8.8 6 5.5 Z" fill="var(--navy)"/></svg>
        07 3190 4627
      </p>
      <p class="contact-item">
        <svg width="18" height="18" viewBox="0 0 18 18"><circle cx="9" cy="9" r="8" fill="none" stroke="var(--navy)" stroke-width="1.5"/><path d="M9 4 C7 4 5.8 5.4 5.8 7 C5.8 9.2 9 13 9 13 C9 13 12.2 9.2 12.2 7 C12.2 5.4 11 4 9 4 Z" fill="var(--navy)"/><circle cx="9" cy="7" r="1.2" fill="#fff"/></svg>
        48 Banksia Crescent<br>(off Wattle Glen BLVD)<br>Hollydale QLD 4188
      </p>
      <p class="contact-item contact-web">
        <svg width="18" height="18" viewBox="0 0 18 18"><circle cx="9" cy="9" r="8" fill="none" stroke="var(--navy)" stroke-width="1.5"/><rect x="5" y="6" width="8" height="6" rx="1" fill="var(--navy)"/><path d="M5.3 6.4 L9 9.3 L12.7 6.4" fill="none" stroke="#fff" stroke-width="1"/></svg>
        www.wattleglenmanor.com.au
      </p>
    </div>
  </section>

  <section class="panel panel-cover">
    <svg class="shapes" width="380" height="779" viewBox="0 0 380 779">
      <defs>
        <linearGradient id="courtyardTone" x1="0" y1="0" x2="0" y2="1">
          <stop offset="0" stop-color="#7fb0d8"/>
          <stop offset=".45" stop-color="#5f7f4a"/>
          <stop offset=".75" stop-color="#a88e6e"/>
          <stop offset="1" stop-color="#c6c9cc"/>
        </linearGradient>
      </defs>
      <rect y="150" width="380" height="400" fill="url(#courtyardTone)" role="img" aria-label="Photo of the landscaped courtyard with pergola, garden and paved walkway"/>
      <path d="M0,0 L380,0 L380,120 C380,160 360,178 320,178 L0,178 Z" fill="var(--sky)"/>
      <path d="M0,0 L366,0 L366,112 C366,150 346,168 306,168 L0,168 Z" fill="var(--navy)"/>
      <rect y="528" width="380" height="110" fill="var(--sky)"/>
      <rect y="646" width="380" height="133" fill="var(--navy)"/>
      <rect y="638" width="380" height="8" fill="var(--sky-light)"/>
    </svg>
    <div class="content cover-brand">
      <div class="brand"><span class="brand-dot"></span><span class="brand-name">Wattle Glen Manor</span></div>
      <p class="cover-line">At Wattle Glen Manor,<small>we're committed to your care and comfort</small></p>
    </div>
    <h1 class="content cover-headline">Providing aged care with quality,<br>dignity and individuality</h1>
    <p class="content cover-web">www.wattleglenmanor.com.au</p>
  </section>

</main>
</body>
</html>
```